Meadowlark Suds Business Card

The new business card design will incorporate my new logo components designed by one of your designers. Meadowlark Suds creates high quality soaps and bath products. They would be suited for a Spa, Bed and Breakfast, Boutique environment. The look should be a white background.
Classy, soft and using the colour palet of the logo. The card will be two sided.
Updates

Target Market(s)

Looking to appeal to an upper end market. Spas, boutiques, independent gift stores, bridal salons, bed and breakfast, etc. I want the card to impart a sense of elegance, tranquility and Meadowlark. But also quality and value.

Industry/Entity Type

Business

Font styles to use
Sans Serif
Script

Requirements
Must have
• My logo on the front. But also on the back but faded out to allow written notes on the back.
On the front : Carla Penwick
Owner/Creator
47 Ashgrove Rd
Larkfield, Ont K4R 2P9
613.402.9186
Creating Quality Handcrafted Soaps And Bath Products
Custom and Wholesale Orders Welcome
Www.meadowlarksuds-example.ca
Www.facebook.com / MeadowlarkSudsandTub
info@meadowlarksuds-example.ca

```html
<!DOCTYPE html>
<html lang="en">
<head>
<meta charset="utf-8">
<title>Meadowlark Suds – Business Card</title>
<link rel="stylesheet" href="https://fonts.googleapis.com/css2?family=Arimo&family=Open+Sans:ital,wght@0,400;1,300;1,400&family=Italianno&display=swap">
<style>
  :root {
    --teal: #8fbab0;
    --teal-soft: #a9cfc7;
    --teal-mist: #e6f1ee;
    --sand: #e2d5c3;
    --ink: #222222;
    --ink-soft: #333333;
    --paper: #ffffff;
    --rule: #ead9c8;
  }
  * { margin: 0; padding: 0; box-sizing: border-box; }
  html, body {
    width: 1017px; height: 1200px; overflow: hidden;
    background: var(--paper);
  }
  .sheet { position: relative; width: 1017px; height: 1200px; }

  .card {
    position: absolute; left: 87px; width: 855px; height: 488px;
    overflow: hidden;
  }
  .card--front { top: 59px; background: var(--paper); }
  .card--back {
    top: 632px;
    background: linear-gradient(90deg,
      var(--teal-soft) 0%, #d6e9e4 12%, var(--paper) 30%,
      var(--paper) 72%, #d9ebe7 84%, var(--teal-soft) 100%);
  }

  .front-sweep { position: absolute; inset: 0; width: 100%; height: 100%; }

  .logo-art {
    position: absolute;
    background: radial-gradient(ellipse at 50% 42%, var(--teal-mist) 0%, #dcebe6 40%, rgba(226,213,195,0.35) 62%, rgba(255,255,255,0) 72%);
  }
  .card--front .logo-art { left: 40px; top: 36px; width: 300px; height: 250px; }
  .card--back .logo-art { left: 262px; top: 30px; width: 320px; height: 240px; }

  .brand-name {
    position: absolute;
    font-family: "Open Sans", sans-serif; font-style: normal; font-weight: 400;
    color: var(--teal); font-size: 32px; white-space: nowrap;
    display: flex; align-items: center; gap: 10px;
  }
  .brand-name::before {
    content: ""; width: 10px; height: 10px; border-radius: 50%;
    background: var(--teal);
  }
  .card--front .brand-name { left: 40px; top: 292px; }
  .card--back .brand-name { left: 50%; top: 270px; transform: translateX(-50%); }

  .owner {
    position: absolute; right: 20px; top: 22px; text-align: right;
    font-family: "Arimo", sans-serif;
  }
  .owner__name { font-size: 35px; color: var(--ink); line-height: 1.1; }
  .owner__rule { height: 1px; background: var(--rule); margin: 4px 0 5px 8px; }
  .owner__role { font-size: 14px; color: var(--ink-soft); }

  .contact {
    font-family: "Open Sans", sans-serif; font-style: italic; color: var(--ink-soft);
  }
  .contact__line { font-weight: 300; }
  .contact__web { font-weight: 400; }
  .card--front .contact {
    position: absolute; right: 20px; top: 242px; text-align: right;
  }
  .card--front .contact__line { font-size: 27px; line-height: 34px; }
  .card--front .contact__web { font-size: 16.5px; line-height: 24px; }

  .tagline {
    position: absolute; font-family: "Italianno", cursive;
    color: var(--ink-soft); white-space: nowrap;
  }
  .card--front .tagline { right: 20px; top: 428px; font-size: 38px; }
  .card--back .tagline { left: 50%; top: 338px; transform: translateX(-50%); font-size: 38px; }

  .card--back .contact {
    position: absolute; left: 0; right: 0; top: 383px; text-align: center;
  }
  .card--back .contact__line { font-size: 17.5px; line-height: 23px; }
  .card--back .contact__web { font-size: 14px; line-height: 19px; }
</style>
</head>
<body>
<main class="sheet">

  <section class="card card--front" aria-label="Business card front">
    <svg class="front-sweep" viewBox="0 0 855 488" preserveAspectRatio="none" aria-hidden="true">
      <defs>
        <linearGradient id="sweepFill" x1="0" y1="0.6" x2="1" y2="1">
          <stop offset="0" stop-color="#ffffff"/>
          <stop offset="0.35" stop-color="#eef5f3"/>
          <stop offset="0.7" stop-color="#d9eae6"/>
          <stop offset="1" stop-color="#a9cfc7"/>
        </linearGradient>
      </defs>
      <path d="M20 488 C 330 430, 560 300, 612 0 L 855 0 L 855 488 Z" fill="url(#sweepFill)"/>
    </svg>

    <div class="logo-art" role="img" aria-label="Brand tree illustration with soft teal, sand and grey leaf dabs"></div>
    <div class="brand-name">Meadowlark Suds</div>

    <div class="owner">
      <div class="owner__name">Carla Penwick</div>
      <div class="owner__rule"></div>
      <div class="owner__role">Owner/Creator</div>
    </div>

    <address class="contact">
      <div class="contact__line">47 Ashgrove Rd</div>
      <div class="contact__line">Larkfield, Ont K4R 2P9</div>
      <div class="contact__line">Tel : 613.402.9186</div>
      <div class="contact__web">www.meadowlarksuds-example.ca</div>
      <div class="contact__web">www.facebook.com / MeadowlarkSudsandTub</div>
    </address>

    <p class="tagline">Creating Quality Handcrafted Soaps And Bath Products</p>
  </section>

  <section class="card card--back" aria-label="Business card back">
    <div class="logo-art" role="img" aria-label="Brand tree illustration with soft teal, sand and grey leaf dabs"></div>
    <div class="brand-name">Meadowlark Suds</div>

    <p class="tagline">Creating Quality Handcrafted Soaps And Bath Products</p>

    <address class="contact">
      <div class="contact__line">47 Ashgrove Rd Larkfield, Ont K4R 2P9</div>
      <div class="contact__line">Tel : 613.402.9186</div>
      <div class="contact__web">www.meadowlarksuds-example.ca</div>
      <div class="contact__web">www.facebook.com / MeadowlarkSudsandTub</div>
    </address>
  </section>

</main>
</body>
</html>
```